Dale Harwick Realtors
Stationary, Letterhead, Business Cards & Envelopes
Modern
Dale Harwick
Broker/ Owner
5817 Elmwood Crest Rd.
Fort Worth, Texas 76243
daleharwick@vesnamail.net
www.DaleHarwickRealtors.com
I would like the back to be the logo and I am not sure if it should have a white background or some color, I am open.
use logo here

```html
<!DOCTYPE html>
<html lang="en">
<head>
<meta charset="utf-8">
<title>Dale Harwick Realtors — Business Card</title>
<link href="https://fonts.googleapis.com/css2?family=Cinzel:wght@400;500&family=Cormorant+SC:wght@500&display=swap" rel="stylesheet">
<style>
  :root {
    --page: #e9ebee;
    --card: #ffffff;
    --navy: #1d3f73;
    --blue: #2f6fb0;
    --blue-light: #6fa3d6;
    --blue-deep: #174a86;
    --charcoal: #2d2f33;
    --text: #3b4a5e;
  }
  * { box-sizing: border-box; margin: 0; padding: 0; }
  html, body { width: 1200px; height: 980px; overflow: hidden; }
  body {
    background: var(--page);
    display: flex;
    flex-direction: column;
    align-items: center;
    justify-content: center;
    gap: 22px;
  }
  .card {
    position: relative;
    width: 800px;
    height: 457px;
    background: var(--card);
    border-radius: 22px;
    overflow: hidden;
    box-shadow: 0 2px 10px rgba(0,0,0,0.10);
  }
  .card__swoosh { position: absolute; inset: 0; }
  .brand {
    display: flex;
    align-items: center;
    gap: 14px;
    font-family: "Cinzel", serif;
    font-weight: 500;
    color: var(--navy);
  }
  .brand__mark {
    width: 34px; height: 34px;
    background: var(--navy);
    flex: none;
  }
  .brand__name { font-size: 34px; letter-spacing: 1px; line-height: 1; }
  .brand__name small { display: block; font-size: 14px; letter-spacing: 6px; margin-top: 8px; text-align: center; }
  .card--front .brand { position: absolute; left: 42px; top: 92px; }
  .contact {
    position: absolute;
    left: 42px;
    top: 200px;
    list-style: none;
    font-family: "Cormorant SC", serif;
    font-weight: 500;
    font-size: 15px;
    color: var(--text);
    letter-spacing: 0.5px;
  }
  .contact li { display: flex; align-items: center; gap: 10px; height: 22px; }
  .contact svg { width: 14px; height: 14px; flex: none; }
  .signature {
    position: absolute;
    right: 44px;
    bottom: 38px;
    text-align: right;
    font-family: "Cinzel", serif;
    color: var(--navy);
  }
  .signature__name { font-size: 19px; letter-spacing: 1px; }
  .signature__role { font-family: "Cormorant SC", serif; font-size: 15px; letter-spacing: 1px; margin-top: 4px; }
  .card--back { display: flex; align-items: center; justify-content: center; }
  .card--back .brand__name { font-size: 44px; }
  .card--back .brand__name small { font-size: 17px; }
  .card--back .brand__mark { width: 44px; height: 44px; }
</style>
</head>
<body>

<section class="card card--front">
  <svg class="card__swoosh" viewBox="0 0 800 457" aria-hidden="true">
    <defs>
      <linearGradient id="swooshBlue" x1="0" y1="0" x2="1" y2="1">
        <stop offset="0" stop-color="var(--blue-light)"/>
        <stop offset="0.5" stop-color="var(--blue)"/>
        <stop offset="1" stop-color="var(--blue-deep)"/>
      </linearGradient>
    </defs>
    <path d="M250 0 C430 20 690 150 800 370 L800 0 Z" fill="var(--charcoal)"/>
    <path d="M278 0 C450 22 700 150 800 350 L800 0 Z" fill="url(#swooshBlue)"/>
  </svg>

  <div class="brand">
    <span class="brand__mark"></span>
    <span class="brand__name">Dale Harwick<small>Realtors</small></span>
  </div>

  <ul class="contact">
    <li><svg viewBox="0 0 14 14"><circle cx="7" cy="7" r="7" fill="var(--navy)"/><path d="M7 3.2a2.4 2.4 0 0 0-2.4 2.4C4.6 7.4 7 10.8 7 10.8s2.4-3.4 2.4-5.2A2.4 2.4 0 0 0 7 3.2z" fill="#fff"/></svg>5817 Elmwood Crest Rd.</li>
    <li><svg viewBox="0 0 14 14"><circle cx="7" cy="7" r="7" fill="var(--navy)"/><rect x="4" y="4" width="6" height="6" fill="#fff"/></svg>Fort Worth, Texas 76243</li>
    <li><svg viewBox="0 0 14 14"><circle cx="7" cy="7" r="7" fill="var(--navy)"/><path d="M4.3 3.8h1.8l.7 1.8-1 .7a5 5 0 0 0 2 2l.7-1 1.8.7v1.8A5.8 5.8 0 0 1 4.3 3.8z" fill="#fff"/></svg>817-555-0142</li>
    <li><svg viewBox="0 0 14 14"><circle cx="7" cy="7" r="7" fill="var(--navy)"/><path d="M4.3 3.8h1.8l.7 1.8-1 .7a5 5 0 0 0 2 2l.7-1 1.8.7v1.8A5.8 5.8 0 0 1 4.3 3.8z" fill="#fff"/></svg>817-555-0187</li>
    <li><svg viewBox="0 0 14 14"><circle cx="7" cy="7" r="7" fill="var(--navy)"/><rect x="3.5" y="4.5" width="7" height="5" fill="#fff"/><path d="M3.5 4.5 7 7.4l3.5-2.9" fill="none" stroke="var(--navy)" stroke-width="0.8"/></svg>daleharwick@vesnamail.net</li>
    <li><svg viewBox="0 0 14 14"><circle cx="7" cy="7" r="7" fill="var(--navy)"/><circle cx="7" cy="7" r="3.6" fill="none" stroke="#fff" stroke-width="0.9"/><path d="M3.4 7h7.2M7 3.4c-1.6 2-1.6 5.2 0 7.2M7 3.4c1.6 2 1.6 5.2 0 7.2" fill="none" stroke="#fff" stroke-width="0.7"/></svg>www.DaleHarwickRealtors.com</li>
  </ul>

  <div class="signature">
    <div class="signature__name">Dale Harwick</div>
    <div class="signature__role">Broker/ Owner</div>
  </div>
</section>

<section class="card card--back">
  <div class="brand">
    <span class="brand__mark"></span>
    <span class="brand__name">Dale Harwick<small>Realtors</small></span>
  </div>
</section>

</body>
</html>
```